VoxTend Needs a Business Card

We need a business card for Tomas Belcourt, Ph.D., CCC-SLP, who is affiliated with Harrowfield Crest University. He is an Associate Professor and Licensed Speech-Language Pathologist, Department of Communication Disorders, College of Health and Human Services.

He has a consulting business "VoxTend Consultant". The logo is attached. The consulting company color is Turquoise. HCU school color is orange.

The consulting business focus on: Consultation, Research & Professional Development. Our target market is individuals with annual family income of $100,000.00 or more for consultation and speech-language pathologists for professional development activities.

No harsh colors, subtle colors appreciated. Address, e-mail, telephone, and small scan logo for a link to our website. Creativity in design will be appreciated. Please add your comments, why you created this design?

Thanks and looking for submissions.

```html
<!DOCTYPE html>
<html lang="en">
<head>
<meta charset="utf-8">
<title>VoxTend Consultant — Business Card</title>
<link rel="stylesheet" href="https://fonts.googleapis.com/css2?family=Open+Sans:wght@300;400;600&display=swap">
<style>
  :root {
    --backdrop: #ecebea;
    --card: #ffffff;
    --turquoise: #4fbfc7;
    --turquoise-soft: #a6dde2;
    --leaf: #5cb85c;
    --orange: #eea45a;
    --ink-soft: #8a9a9c;
    --hairline: #a6dde2;
    --shadow: rgba(60, 60, 60, 0.12);
  }
  * { margin: 0; padding: 0; box-sizing: border-box; }
  html, body {
    width: 1200px;
    height: 900px;
    overflow: hidden;
    background: var(--backdrop);
    font-family: "Open Sans", Arial, sans-serif;
  }
  .canvas { position: relative; width: 1200px; height: 900px; }
  .card {
    position: absolute;
    width: 620px;
    height: 354px;
    background: var(--card);
    box-shadow: 0 6px 18px var(--shadow);
    overflow: hidden;
  }

  /* Front side */
  .card--front { left: 90px; top: 90px; }
  .brand {
    position: absolute;
    left: 130px;
    top: 138px;
    display: flex;
    align-items: center;
    gap: 18px;
  }
  .brand__mark { width: 56px; height: 56px; background: var(--turquoise); }
  .brand__name {
    font-weight: 300;
    font-size: 34px;
    color: var(--turquoise);
    letter-spacing: 0.2px;
  }
  .front__rule {
    position: absolute;
    left: 190px;
    top: 270px;
    width: 250px;
    height: 1px;
    background: var(--hairline);
  }
  .front__web {
    position: absolute;
    left: 0; right: 0;
    top: 280px;
    text-align: center;
    font-size: 13px;
    color: var(--leaf);
    letter-spacing: 0.4px;
  }

  /* Back side */
  .card--back { left: 490px; top: 456px; }
  .back__accent {
    position: absolute;
    right: 40px;
    top: -20px;
    width: 150px;
    height: 150px;
    background: var(--turquoise-soft);
  }
  .holder { position: absolute; left: 44px; top: 56px; width: 340px; }
  .holder__name { font-weight: 400; font-size: 20px; line-height: 26px; color: var(--turquoise); }
  .holder__role {
    margin-top: 4px;
    font-weight: 600;
    font-size: 10px;
    line-height: 16px;
    letter-spacing: 2.4px;
    color: var(--leaf);
    text-transform: uppercase;
  }
  .affiliation { position: absolute; left: 44px; top: 140px; width: 340px; }
  .affiliation__rule { width: 36px; height: 2px; background: var(--orange); margin-bottom: 8px; }
  .affiliation__school { font-weight: 600; font-size: 12.5px; line-height: 18px; color: var(--orange); }
  .affiliation__dept { font-size: 11px; line-height: 16px; color: var(--ink-soft); }
  .contact {
    position: absolute;
    left: 44px;
    top: 234px;
    list-style: none;
    font-size: 12.5px;
    line-height: 18px;
    color: var(--leaf);
  }
  .contact__gap { margin-top: 6px; }
  .scan-code {
    position: absolute;
    right: 40px;
    bottom: 30px;
    width: 78px;
    height: 78px;
    background: var(--card);
    border: 2px solid var(--turquoise);
    padding: 8px;
  }
  .scan-code__field { width: 100%; height: 100%; background: linear-gradient(135deg, var(--turquoise-soft), var(--turquoise)); }
</style>
</head>
<body>
  <main class="canvas">
    <section class="card card--front" aria-label="Card front">
      <div class="brand">
        <div class="brand__mark"></div>
        <span class="brand__name">VoxTend Consultant</span>
      </div>
      <div class="front__rule"></div>
      <p class="front__web">www.voxtend.com</p>
    </section>

    <section class="card card--back" aria-label="Card back">
      <div class="back__accent"></div>
      <div class="holder">
        <h1 class="holder__name">Tomas Belcourt PhD CCC-SLP</h1>
        <p class="holder__role">Associate Professor</p>
        <p class="holder__role">Licensed Speech-Language Pathologist</p>
      </div>
      <div class="affiliation">
        <div class="affiliation__rule"></div>
        <p class="affiliation__school">Harrowfield Crest University</p>
        <p class="affiliation__dept">Dept. of Communication Disorders</p>
        <p class="affiliation__dept">College of Health and Human Services</p>
      </div>
      <ul class="contact">
        <li>418 Linden Row, Suite 3,</li>
        <li>Harrowfield, IL 60466</li>
        <li class="contact__gap">555 010 247</li>
        <li>hello@voxtend.com</li>
        <li>www.voxtend.com</li>
      </ul>
      <div class="scan-code" role="img" aria-label="Scan code linking to the VoxTend website">
        <div class="scan-code__field"></div>
      </div>
    </section>
  </main>
</body>
</html>
```